Aunt Rolina's Bakery

I am about to create a luxury boutique that specializes in cake baking and cupcake
and ready for parties and special events and order delivery
the logo has already made

Industry/Entity Type

Boutique

Contact Information for Business Card

Email:auntrolinasbakery@maplecrumbmail.com
Instagram: aunt_rolina_bakery
Twitter: xxxxxxx
WhatsApp: xxxxxxx

Requirements
Must have
• luxury design

```html
<!DOCTYPE html>
<html lang="en">
<head>
<meta charset="utf-8">
<title>Aunt Rolina's Bakery – Business Card Options</title>
<link rel="stylesheet" href="https://fonts.googleapis.com/css2?family=Lora:wght@400&family=Open+Sans:wght@400&display=swap">
<style>
  :root {
    --stage: #ebecec;
    --ink: #2a2a2a;
    --taupe: #7c7873;
    --text-grey: #5d5a58;
    --rose: #d996aa;
    --rose-deep: #dc94ab;
    --blush: #f3dde3;
    --white: #ffffff;
    --shadow: rgba(0,0,0,0.22);
  }
  * { box-sizing: border-box; margin: 0; padding: 0; }
  html, body { width: 1200px; height: 864px; overflow: hidden; background: var(--stage); }
  .stage { position: relative; width: 1200px; height: 864px; }
  .option-number {
    position: absolute; top: 24px; width: 40px; text-align: center;
    font: 400 34px "Open Sans", sans-serif; color: var(--ink);
  }
  .card {
    position: absolute; width: 427px; height: 683px; border-radius: 42px;
    overflow: hidden; box-shadow: 0 8px 14px var(--shadow);
  }
  .card > * { position: absolute; }
  .centered { left: 0; width: 100%; text-align: center; }
  .ornament { background: var(--taupe); opacity: 0.28; border-radius: 30px; }
  .rule { height: 3px; background: var(--rose); }

  /* Card one */
  .card-one { left: 106px; top: 107px;
    background: linear-gradient(to bottom, var(--white) 0%, var(--white) 30%, #f4e1e6 50%, #e9bcc9 75%, var(--rose-deep) 100%); }
  .card-one .brand-name { font: 400 36px/1 "Lora", serif; color: var(--taupe); letter-spacing: 0.5px; }
  .card-one .brand-sub { font: 400 19px/1 "Lora", serif; color: var(--taupe); letter-spacing: 14px; text-indent: 14px; }
  .card-one .contact { font: 400 17px/1 "Lora", serif; color: var(--text-grey); }
  .card-one .social { background: var(--white); }
  .card-one .pattern-band { left: 0; bottom: 0; width: 100%; height: 70px;
    background: linear-gradient(to bottom, rgba(255,255,255,0.15), rgba(255,255,255,0.35)); }

  /* Card two */
  .card-two { left: 650px; top: 111px;
    background: linear-gradient(to bottom, var(--white) 0, var(--white) 222px, var(--blush) 222px); }
  .card-two .band { left: 0; top: 222px; width: 100%; height: 41px; background: var(--rose); }
  .card-two .band-inner { left: 0; top: 233px; width: 100%; height: 19px; background: var(--white); }
  .card-two .frame { left: 50px; top: 88px; width: 331px; height: 307px; filter: drop-shadow(0 2px 3px rgba(0,0,0,0.2)); }
  .card-two .brand-name { font: 400 31px/1 "Open Sans", sans-serif; color: var(--taupe); }
  .card-two .brand-sub { font: 400 17px/1 "Open Sans", sans-serif; color: var(--taupe); letter-spacing: 11px; text-indent: 11px; }
  .card-two .contact { font: 400 18px/1 "Open Sans", sans-serif; color: var(--text-grey); }
  .card-two .social { background: var(--rose); }

  .emblem { border-radius: 50%; background: var(--rose); border: 3px solid var(--white); box-shadow: 0 0 0 2px var(--taupe); }
  .social-row { display: flex; justify-content: center; gap: 14px; }
  .social { width: 45px; height: 45px; border-radius: 50%; }
  .mail-icon { display: inline-block; vertical-align: middle; margin-right: 8px; }
</style>
</head>
<body>
<main class="stage">
  <div class="option-number" style="left:296px">1</div>
  <div class="option-number" style="left:857px">2</div>

  <!-- Option one -->
  <section class="card card-one" aria-label="Business card option one">
    <div class="ornament" role="img" aria-label="Scrollwork flourish, left" style="left:41px; top:128px; width:122px; height:30px"></div>
    <div class="ornament" role="img" aria-label="Scrollwork flourish, right" style="left:263px; top:128px; width:122px; height:30px"></div>
    <div class="emblem" style="left:164px; top:49px; width:98px; height:98px"></div>
    <div class="rule" style="left:41px; top:170px; width:344px"></div>
    <div class="brand-name centered" style="top:180px">AUNT ROLINA'S</div>
    <div class="rule" style="left:41px; top:225px; width:344px"></div>
    <div class="brand-sub centered" style="top:236px">BAKERY</div>
    <div class="rule" style="left:118px; top:261px; width:190px; height:2px"></div>
    <div class="ornament" role="img" aria-label="Scrollwork flourish below the name" style="left:130px; top:272px; width:166px; height:52px"></div>

    <p class="contact centered" style="top:374px">
      <svg class="mail-icon" width="20" height="13" viewBox="0 0 20 13"><rect x="0.75" y="0.75" width="18.5" height="11.5" fill="none" stroke="#5d5a58" stroke-width="1.5"/><path d="M1 1 L10 7.5 L19 1" fill="none" stroke="#5d5a58" stroke-width="1.5"/></svg>auntrolinasbakery@maplecrumbmail.com
    </p>
    <div class="social-row centered" style="top:429px">
      <span class="social"></span><span class="social"></span><span class="social"></span>
    </div>
    <p class="contact centered" style="top:490px">aunt_rolina_bakery</p>
    <div class="pattern-band" role="img" aria-label="Band of light swirl pattern along the bottom edge"></div>
  </section>

  <!-- Option two -->
  <section class="card card-two" aria-label="Business card option two">
    <div class="band"></div>
    <div class="band-inner"></div>
    <svg class="frame" viewBox="0 0 331 307" aria-hidden="true">
      <path d="M40 18 Q165 18 165 4 Q165 18 291 18 Q291 40 313 40 L313 267 Q291 267 291 289 Q165 289 165 303 Q165 289 40 289 Q40 267 18 267 L18 40 Q40 40 40 18 Z" fill="#ffffff" stroke="#d996aa" stroke-width="9"/>
      <path d="M48 27 Q165 27 165 15 Q165 27 283 27 Q283 48 304 48 L304 259 Q283 259 283 280 Q165 280 165 292 Q165 280 48 280 Q48 259 27 259 L27 48 Q48 48 48 27 Z" fill="none" stroke="#d996aa" stroke-width="1.5"/>
    </svg>
    <div class="ornament" role="img" aria-label="Scrollwork flourish, left" style="left:80px; top:182px; width:90px; height:26px"></div>
    <div class="ornament" role="img" aria-label="Scrollwork flourish, right" style="left:257px; top:182px; width:90px; height:26px"></div>
    <div class="emblem" style="left:173px; top:123px; width:80px; height:80px"></div>
    <div class="rule" style="left:80px; top:220px; width:267px; height:2px"></div>
    <div class="brand-name centered" style="top:227px">AUNT ROLINA'S</div>
    <div class="rule" style="left:80px; top:265px; width:267px; height:2px"></div>
    <div class="brand-sub centered" style="top:273px">BAKERY</div>
    <div class="rule" style="left:140px; top:296px; width:147px; height:2px"></div>
    <div class="ornament" role="img" aria-label="Scrollwork flourish below the name" style="left:152px; top:305px; width:122px; height:40px"></div>

    <p class="contact centered" style="top:442px">
      <svg class="mail-icon" width="20" height="13" viewBox="0 0 20 13"><rect x="0.75" y="0.75" width="18.5" height="11.5" fill="none" stroke="#5d5a58" stroke-width="1.5"/><path d="M1 1 L10 7.5 L19 1" fill="none" stroke="#5d5a58" stroke-width="1.5"/></svg>auntrolinasbakery@maplecrumbmail.com
    </p>
    <div class="social-row centered" style="top:498px">
      <span class="social"></span><span class="social"></span><span class="social"></span>
    </div>
    <p class="contact centered" style="top:556px">aunt_rolina_bakery</p>
  </section>
</main>
</body>
</html>
```